CREATE A 2 layout and logo ( velunarix )

I need to create 2 layout for my company being a homepage will be like and other client control panel and need to create the logo of the company, my company works with website hosting and sale of dedicated server and VPS cloud the company name and velunarix, I want the site to be very accessible and that is not too flashy

Target Market(s)

website hosting

Industry/Entity Type

It Company

Number of Pages Required

2 page

Font styles to use
Sans Serif

Requirements
Must have
• domain velunarix.example
Nice to have
• banners, login area, login webmail
Should not have
• no preference

```html
<!DOCTYPE html>
<html lang="en">
<head>
<meta charset="utf-8">
<title>velunarix – Cloud Hosting</title>
<link rel="stylesheet" href="https://fonts.googleapis.com/css2?family=Cabin:ital,wght@0,400;0,500;0,600;0,700;1,400;1,500&display=swap">
<style>
:root{
  --blue:#2a93d5;
  --blue-dark:#1f7fc0;
  --link:#1a8ad0;
  --ink:#222;
  --text:#555;
  --muted:#777;
  --header-bg:#f6f6f6;
  --panel:#eeeeee;
  --rule:#e2e2e2;
  --bullet:#e5484d;
}
*{box-sizing:border-box;margin:0;padding:0}
html,body{width:1200px;height:1150px;overflow:hidden}
body{position:relative;background:#fff;font-family:"Cabin",Arial,sans-serif;color:var(--text)}
a{text-decoration:none;color:inherit}
.abs{position:absolute}

.site-header{position:absolute;left:0;top:0;width:1200px;height:133px;background:var(--header-bg);border-top:4px solid var(--blue)}
.top-tab{position:absolute;left:645px;top:0}
.top-tab__links{position:absolute;left:677px;top:13px;font-size:13px;font-weight:600;color:#fff;display:flex;gap:10px;align-items:center}
.top-tab__search{position:absolute;left:887px;top:10px;width:152px;height:22px;background:#fff;border-radius:2px}
.brand{position:absolute;left:127px;top:58px;font-size:34px;font-weight:500;letter-spacing:7px;color:var(--ink);text-transform:uppercase}
.main-nav{position:absolute;top:94px;left:541px;font-size:14px;color:#444}
.main-nav a,.main-nav span{position:absolute;top:6px;white-space:nowrap}
.main-nav .is-active{top:0;left:0;width:57px;height:29px;background:var(--blue);color:#fff;border-radius:3px;text-align:center;line-height:28px}

.hero{position:absolute;left:0;top:133px;width:1200px;height:359px;background:linear-gradient(100deg,#7b90aa 0%,#c3d0dd 35%,#e4ebf1 55%,#9fb0c2 75%,#2e3b4f 100%)}
.hero__title{position:absolute;left:131px;top:236px;font-size:45px;line-height:53px;font-weight:700;color:#151515;text-shadow:0 1px 2px rgba(255,255,255,.6)}
.hero__dots{position:absolute;left:130px;top:458px;display:flex;gap:11px}
.hero__dots i{width:33px;height:5px;background:#fff}
.hero__dots i:first-child{background:var(--blue)}

.press-bar{position:absolute;left:130px;top:508px;width:940px;height:59px;background:#f4f4f4;border:1px solid #ddd;box-shadow:0 2px 4px rgba(0,0,0,.08)}
.press-bar__label{position:absolute;left:19px;top:20px;font-size:15px;font-weight:600;color:var(--ink)}
.press-bar__text{position:absolute;left:128px;top:22px;font-size:13px;color:var(--link)}
.press-bar__date{position:absolute;left:764px;top:22px;font-size:12px;font-style:italic;color:#444}
.press-bar__arrow{position:absolute;top:19px;width:17px;height:22px;background:#fff;border:1px solid #ccc}

.col{position:absolute;top:604px;font-size:13px;line-height:20px}
.col h2{font-size:24px;font-weight:400;color:var(--ink);margin-bottom:17px}
.col h2 em{font-style:normal;color:var(--link)}
.col-divider{position:absolute;top:622px;width:1px;height:240px;background:var(--rule)}
.about-more{color:var(--link);font-style:italic;font-weight:500;margin-top:4px}
.read-more{position:absolute;top:858px;font-size:16px;color:#444}
.solutions li{list-style:none;display:flex;align-items:center;gap:9px;margin-top:9px}
.solutions li::before{content:"";width:11px;height:11px;border-radius:50%;background:var(--bullet)}
.field{position:absolute;left:793px;width:254px;height:34px;border:1px solid #ccc;border-radius:3px;background:linear-gradient(#fff,#f3f3f3);font-size:13px;font-style:italic;color:#999;padding:9px 13px}
.signup-btn{position:absolute;left:974px;top:826px;width:73px;height:28px;background:var(--blue);border-radius:4px;color:#fff;font-size:13px;font-weight:600;text-align:center;line-height:28px}

.footer-links{position:absolute;left:130px;top:904px;width:940px;height:187px;background:var(--panel);border-radius:3px}
.footer-col{position:absolute;top:16px}
.footer-col h3{font-size:16px;font-weight:500;color:#333;margin-bottom:8px}
.footer-col li{list-style:none;font-size:13px;color:var(--link);line-height:27px;padding-left:20px;position:relative}
.footer-col li::before{content:"→";position:absolute;left:0;font-size:10px;color:#333}

.copyright{position:absolute;left:130px;top:1109px;font-family:Arial,sans-serif;font-size:10px;color:#222}
.copyright span{color:var(--link)}
.social{position:absolute;left:861px;top:1111px;display:flex;gap:12px;align-items:center;font-size:10px;color:#999}
.social i{width:15px;height:15px;border-radius:50%;background:#bbb;display:block}
</style>
</head>
<body>
<header class="site-header">
  <svg class="top-tab" width="426" height="55" viewBox="0 0 426 55" aria-hidden="true">
    <path d="M0 0H426L405 45H21Z" fill="#3a9bd9"/>
    <path d="M30 50H400" stroke="rgba(0,0,0,.08)" stroke-width="4"/>
  </svg>
  <nav class="top-tab__links"><span>United State ▾</span><span>|</span><span>My Account</span></nav>
  <div class="top-tab__search">
    <svg class="abs" style="left:131px;top:3px" width="16" height="16" viewBox="0 0 16 16"><circle cx="6" cy="6" r="4.5" fill="none" stroke="#222" stroke-width="2"/><path d="M9.5 9.5L15 15" stroke="#222" stroke-width="2.5"/></svg>
  </div>
  <a class="brand" href="#">velunarix</a>
  <nav class="main-nav">
    <a class="is-active" href="#">Home</a>
    <span style="left:70px">|</span><a style="left:97px" href="#">About</a>
    <span style="left:202px">|</span><a style="left:228px" href="#">Solutions</a>
    <span style="left:307px">|</span><a style="left:334px" href="#">Press Room</a>
    <span style="left:430px">|</span><a style="left:456px" href="#">Contact us</a>
  </nav>
</header>

<section class="hero" role="img" aria-label="Photo of a businessman touching a glowing cloud icon linked to network nodes">
  <div class="hero__dots"><i></i><i></i><i></i><i></i></div>
</section>
<h1 class="hero__title">We are Cloud Computing<br>Company Providing</h1>

<div class="press-bar">
  <span class="press-bar__label">Press Room :</span>
  <span class="press-bar__text">Nam fermentum vestibulum purus id aliquet. Phasellus dui ante, ultricies et sollicitudin pretium, fermentum ....</span>
  <span class="press-bar__date">April 29, 2013</span>
  <svg class="press-bar__arrow" style="left:879px" viewBox="0 0 17 22"><path d="M11 5L5 11L11 17" fill="none" stroke="#222" stroke-width="2.5"/></svg>
  <svg class="press-bar__arrow" style="left:907px" viewBox="0 0 17 22"><path d="M6 5L12 11L6 17" fill="none" stroke="#222" stroke-width="2.5"/></svg>
</div>

<section class="col" style="left:131px;width:290px">
  <h2>About</h2>
  <p>Vestibulum ante ipsum primis in faucibus orci luctus et ultrices posuere cubilia Curae; Ut et scelerisque ante. Donec erat purus, faucibus vitae congue vel, porttitor nec lectus. Aenean a nibh eget turpis vehicula tempus ac sed massa. Vestibulum dolor nulla, ultrices ac tincidunt sed, laoreet non est.</p>
  <p class="about-more">Lorem ipsum dolor sit amet, consectetur adipiscing elit..</p>
</section>
<a class="read-more" style="left:337px" href="#">Read More</a>
<div class="col-divider" style="left:439px"></div>

<section class="col solutions" style="left:461px;width:290px">
  <h2>Our <em>Solutions</em></h2>
  <p>Ut et scelerisque ante. Donec erat purus, faucibus vitae congue vel, porttitor nec lectus.</p>
  <ul style="margin-top:2px"><li>Storage</li><li>Backup &amp; Recovery</li><li>Cloud Computing</li><li>Big Data</li><li>Security</li></ul>
</section>
<a class="read-more" style="left:660px" href="#">Read More</a>
<div class="col-divider" style="left:770px"></div>

<section class="col" style="left:792px;width:270px">
  <h2>Newsletter <em>Signup</em></h2>
  <p>Subscribe to our e-Newsletter today to receive the latest issue, news, stories, events<br>and more.</p>
</section>
<div class="field" style="top:724px">Enter Name</div>
<div class="field" style="top:777px">Enter Email</div>
<p class="abs" style="left:793px;top:820px;width:170px;font-size:13px;line-height:20px">Your email address will not be shared with any third party.</p>
<a class="signup-btn" href="#">SIGN UP</a>

<footer class="footer-links">
  <div class="footer-col" style="left:26px"><h3>Footer Link</h3><ul><li>Aenean a nibh eget</li><li>Vestibulum dolor</li><li>Etiam risus massa</li><li>Aenean a nibh eget</li><li>Vestibulum dolor</li></ul></div>
  <div class="footer-col" style="left:261px"><h3>Footer Link</h3><ul><li>Aenean a nibh eget</li><li>Vestibulum dolor</li><li>Etiam risus massa</li><li>Aenean a nibh eget</li><li>Vestibulum dolor</li></ul></div>
  <div class="footer-col" style="left:497px"><h3>Footer Link</h3><ul><li>Aenean a nibh eget</li><li>Vestibulum dolor</li><li>Etiam risus massa</li><li>Aenean a nibh eget</li><li>Vestibulum dolor</li></ul></div>
  <div class="footer-col" style="left:732px"><h3>Footer Link</h3><ul><li>Aenean a nibh eget</li><li>Vestibulum dolor</li><li>Etiam risus massa</li><li>Aenean a nibh eget</li><li>Vestibulum dolor</li></ul></div>
</footer>

<p class="copyright">Copyright &nbsp;2015 <span>velunarix.example</span>. All Right Reserved.</p>
<div class="social" aria-label="Social links">
  <i></i><i></i><i></i><i></i><i></i><span>⁞ RSS</span>
  <svg width="13" height="13" viewBox="0 0 13 13"><circle cx="2" cy="11" r="2" fill="#aaa"/><path d="M1 6a6 6 0 0 1 6 6M1 1a11 11 0 0 1 11 11" fill="none" stroke="#aaa" stroke-width="2"/></svg>
</div>
</body>
</html>
```